Awesome, colorful pamphlet advertising services for disabled people and supporters

My business, The Ability Crossroads, provides nutritional counseling services to people with and without disabilities throughout the lifespan. It also offers disability consulting, body image coaching and accessible recreation consultation. I would like something representing both children and adults which ties these activities together in a happy way.

Font styles to use
Sans Serif

Colors
00AB8E
00BBA5
67D7C9
C6EFE9
E9F9F6
FFF300
FFF600
FEFA6F
FFFEC7
FFFEE8
F0912C
F2A743
F7CA91
FBE8D2
FDF5EE
E54698
E96AAD
F1A4CE
F9D9EA
FCEFF6
6B429C
8869AF
B7A5CE
E3DAEB
F3F0F8

```html
<!DOCTYPE html>
<html lang="en">
<head>
<meta charset="utf-8">
<title>The Ability Crossroads – Nutritional Counseling Brochure</title>
<link href="https://fonts.googleapis.com/css2?family=Barlow+Condensed:wght@600;700&family=Inter:wght@400;500;600;700&display=swap" rel="stylesheet">
<style>
  :root{
    --ink:#2a1a4c;
    --teal:#00BBA5;
    --teal-dark:#00AB8E;
    --yellow:#FFF300;
    --pink:#E54698;
    --orange:#F0912C;
    --orange-arrow:#EA5A2A;
    --green-arrow:#3DBE7A;
    --paper:#ffffff;
    --rule:#dcdce2;
    --bg:#ececee;
  }
  *{box-sizing:border-box;margin:0;padding:0}
  html,body{width:1200px;height:1200px;overflow:hidden;background:var(--bg)}
  body{position:relative;font-family:'Inter',sans-serif}
  .panel{position:absolute;top:305px;width:280px;height:590px;overflow:hidden}
  .panel--founder{left:12px;background:var(--ink)}
  .panel--cover{left:300px;background:var(--ink)}
  .panel--orgs{left:620px;background:var(--paper);border:1px solid #d6d6dc}
  .panel--people{left:908px;background:var(--paper);border:1px solid #d6d6dc}
  .panel svg.art{position:absolute;inset:0;width:280px;height:590px}
  .display{font-family:'Barlow Condensed',sans-serif;font-weight:700;text-transform:uppercase;line-height:1;letter-spacing:.2px}
  .tag{display:inline-block;padding:1px 3px 0;color:#fff}
  .tag--warm{background:linear-gradient(90deg,var(--pink),var(--orange))}
  .tag--cool{background:linear-gradient(90deg,var(--teal),var(--yellow))}

  /* founder panel */
  .founder__title{position:absolute;left:20px;top:58px;color:#fff;font-size:30px}
  .founder__title .tag{margin-top:2px}
  .founder__portrait{position:absolute;left:22px;top:132px;width:70px;height:70px;border-radius:50%;background:radial-gradient(circle at 50% 45%,#c9a08a,#6b4a40);border:2px solid #fff}
  .founder__name{position:absolute;left:20px;top:220px;color:#fff;font-size:8.4px;font-weight:700}
  .founder__bio{position:absolute;left:20px;top:238px;width:236px;color:#e6def2;font-size:7.9px;line-height:1.6}
  .founder__bio p+p{margin-top:7px}
  .founder__web{position:absolute;left:20px;top:560px;color:#fff;font-size:8.2px;font-weight:600;display:flex;align-items:center;gap:5px}

  /* cover panel */
  .cover__title{position:absolute;left:26px;top:345px;color:#fff;font-size:35px}
  .cover__title span{display:block;margin-bottom:5px}
  .cover__brand{position:absolute;right:16px;bottom:22px;display:flex;align-items:center;gap:6px;color:#fff;font-size:10px;font-weight:600}
  .cover__brand i{width:12px;height:12px;border-radius:50%;background:#fff;display:block}

  /* services panels */
  .services__head{position:absolute;left:22px;top:26px;font-size:22px;color:var(--ink)}
  .services__head .tag{margin-right:2px}
  .svc-list{position:absolute;left:22px;width:196px;list-style:none}
  .svc-list li{position:relative;padding:0 0 6px 18px;margin-bottom:8px;border-bottom:1px solid var(--rule);font-size:8.4px;line-height:1.3;color:var(--ink)}
  .svc-list li svg{position:absolute;left:0;top:1px}
  .panel--orgs .svc-list{top:73px}
  .panel--people .svc-list{top:93px}
  .pres__head{position:absolute;left:20px;top:252px;font-size:22px}
  .pres-cols{position:absolute;left:22px;top:292px;width:245px;display:grid;grid-template-columns:1fr 1fr;column-gap:12px}
  .pres-cols ul{list-style:none}
  .pres-cols li{position:relative;padding-left:18px;margin-bottom:13px;font-size:8.4px;line-height:1.3;color:var(--ink)}
  .pres-cols .col-b li{padding-bottom:6px;border-bottom:1px solid var(--rule);margin-bottom:8px}
  .pres-cols li svg{position:absolute;left:0;top:1px}
  .cta{position:absolute;left:22px;top:338px;color:var(--ink)}
  .cta__ask{font-size:13px;font-weight:400}
  .cta__contact{font-size:8.8px;font-weight:700;margin-top:3px}
</style>
</head>
<body>
<svg width="0" height="0" style="position:absolute">
  <defs>
    <linearGradient id="warm" x1="0" y1="0" x2="1" y2="1"><stop offset="0" stop-color="#E54698"/><stop offset="1" stop-color="#F0912C"/></linearGradient>
    <linearGradient id="cool" x1="0" y1="0" x2="1" y2="1"><stop offset="0" stop-color="#00BBA5"/><stop offset="1" stop-color="#FFF300"/></linearGradient>
    <linearGradient id="coolH" x1="0" y1="0" x2="1" y2="0"><stop offset="0" stop-color="#00BBA5"/><stop offset="1" stop-color="#FFF300"/></linearGradient>
    <linearGradient id="photoWarm" x1="0" y1="0" x2="1" y2="1"><stop offset="0" stop-color="#8a7d72"/><stop offset=".6" stop-color="#b49068"/><stop offset="1" stop-color="#d9a64a"/></linearGradient>
    <linearGradient id="photoGrass" x1="0" y1="0" x2="1" y2="1"><stop offset="0" stop-color="#3d7a3a"/><stop offset=".7" stop-color="#6f9a6a"/><stop offset="1" stop-color="#b9c3da"/></linearGradient>
  </defs>
</svg>

<!-- Panel 1: about the founder -->
<section class="panel panel--founder">
  <svg class="art" viewBox="0 0 280 590" aria-hidden="true">
    <path d="M-10 60 A72 72 0 0 1 78 -12" fill="none" stroke="url(#cool)" stroke-width="24"/>
    <path d="M205 0 C184 70 200 185 280 245 V0 Z" fill="url(#photoWarm)" role="img" aria-label="Photo of the founder's workspace, continued from the cover"/>
    <path d="M205 0 C184 70 200 185 280 245" fill="none" stroke="url(#warm)" stroke-width="9"/>
    <path d="M222 590 A56 56 0 0 1 290 520" fill="none" stroke="url(#cool)" stroke-width="22"/>
  </svg>
  <h2 class="display founder__title">About our<br><span class="tag tag--cool">Founder</span></h2>
  <div class="founder__portrait" role="img" aria-label="Portrait photo of the founder"></div>
  <p class="founder__name">Dana Whitfield, MSW, CARSS I,</p>
  <div class="founder__bio">
    <p>Dana has been passionate about disability issues since 2003 when she discovered disability rights and the disability activism community. This changed her life and helped her feel stronger about herself, her disabilities, and her capabilities. In 2011, she became sick with Postural Orthostatic Tachycardia Syndrome. This was severe and life changing. It taught her about the overlap of disability and chronic illness in a way that nothing but experience can.</p>
    <p>She also holds a Melodyroots early childhood music and movement teacher license for babies through age seven, certification as an Adaptive Recreation and Sports Specialist from Brightfield Sports Alliance and RingVoice for seniors group facilitator certification. Lastly, she earned certificates in both working with veterans and their families from Lakeshore State University and a Trauma Informed Clinical Foundation Certificate from the University of Eastbrook. Because she cares about trauma and body image, she is also a certified body image coach for people with and without disabilities/illness.</p>
  </div>
  <p class="founder__web">
    <svg width="10" height="10" viewBox="0 0 10 10" aria-hidden="true"><circle cx="5" cy="5" r="4.3" fill="none" stroke="#fff" stroke-width="1"/><ellipse cx="5" cy="5" rx="1.8" ry="4.3" fill="none" stroke="#fff" stroke-width=".8"/><path d="M.7 5 H9.3" stroke="#fff" stroke-width=".8"/></svg>
    abilitycrossroads.org
  </p>
</section>

<!-- Panel 2: cover -->
<section class="panel panel--cover">
  <svg class="art" viewBox="0 0 280 590" aria-hidden="true">
    <path d="M0 0 H280 V262 Q150 300 0 255 Z" fill="url(#photoWarm)" role="img" aria-label="Photo of a smiling woman in a wheelchair waving at a laptop during a video session"/>
    <path d="M0 255 Q150 300 280 262" fill="none" stroke="url(#coolH)" stroke-width="8"/>
  </svg>
  <h1 class="display cover__title">
    <span>Nutritional</span>
    <span class="tag tag--warm">Counseling</span>
    <span>Services</span>
  </h1>
  <div class="cover__brand"><i></i>The Ability Crossroads</div>
</section>

<!-- Panel 3: services for organizations -->
<section class="panel panel--orgs">
  <svg class="art" viewBox="0 0 280 590" aria-hidden="true">
    <path d="M0 470 Q120 385 280 372 V590 H0 Z" fill="url(#photoGrass)" role="img" aria-label="Photo of a person with a prosthetic leg stretching on green turf"/>
    <path d="M0 470 Q120 385 280 372" fill="none" stroke="url(#coolH)" stroke-width="9"/>
  </svg>
  <h2 class="display services__head"><span class="tag tag--warm">Services</span> for organizations</h2>
  <ul class="svc-list">
    <li><svg width="10" height="9" viewBox="0 0 10 9"><path d="M0 4.5 H8 M4.5 1 L8 4.5 L4.5 8" fill="none" stroke="#EA5A2A" stroke-width="1.4"/></svg>Program Development and Growth Support</li>
    <li><svg width="10" height="9" viewBox="0 0 10 9"><path d="M0 4.5 H8 M4.5 1 L8 4.5 L4.5 8" fill="none" stroke="#EA5A2A" stroke-width="1.4"/></svg>Customized Presentations/Workshops for Staff Development</li>
    <li><svg width="10" height="9" viewBox="0 0 10 9"><path d="M0 4.5 H8 M4.5 1 L8 4.5 L4.5 8" fill="none" stroke="#EA5A2A" stroke-width="1.4"/></svg>Curriculum and Resource Creation Services Based on Your Goals</li>
    <li><svg width="10" height="9" viewBox="0 0 10 9"><path d="M0 4.5 H8 M4.5 1 L8 4.5 L4.5 8" fill="none" stroke="#EA5A2A" stroke-width="1.4"/></svg>Articles, Blog Posts and Other Content on Commission</li>
    <li><svg width="10" height="9" viewBox="0 0 10 9"><path d="M0 4.5 H8 M4.5 1 L8 4.5 L4.5 8" fill="none" stroke="#EA5A2A" stroke-width="1.4"/></svg>Handmade Collage Art and Creative Writing Pieces for your Office/Program</li>
  </ul>
  <h2 class="display pres__head"><span class="tag tag--cool">Presentations</span></h2>
  <div class="pres-cols">
    <ul class="col-a">
      <li><svg width="10" height="9" viewBox="0 0 10 9"><path d="M0 4.5 H8 M4.5 1 L8 4.5 L4.5 8" fill="none" stroke="#3DBE7A" stroke-width="1.4"/></svg>Disability history and culture</li>
      <li><svg width="10" height="9" viewBox="0 0 10 9"><path d="M0 4.5 H8 M4.5 1 L8 4.5 L4.5 8" fill="none" stroke="#3DBE7A" stroke-width="1.4"/></svg>Body esteem and eating disorders as a disability issue</li>
    </ul>
    <ul class="col-b">
      <li><svg width="10" height="9" viewBox="0 0 10 9"><path d="M0 4.5 H8 M4.5 1 L8 4.5 L4.5 8" fill="none" stroke="#3DBE7A" stroke-width="1.4"/></svg>How to build self-definition and self-compassion</li>
      <li><svg width="10" height="9" viewBox="0 0 10 9"><path d="M0 4.5 H8 M4.5 1 L8 4.5 L4.5 8" fill="none" stroke="#3DBE7A" stroke-width="1.4"/></svg>Trauma and disability</li>
    </ul>
  </div>
</section>

<!-- Panel 4: services for individuals -->
<section class="panel panel--people">
  <svg class="art" viewBox="0 0 280 590" aria-hidden="true">
    <path d="M0 372 Q190 372 280 590 H0 Z" fill="url(#photoGrass)" role="img" aria-label="Photo continued: person in light athletic wear stretching toward their feet"/>
    <path d="M280 328 A56 56 0 0 0 262 425" fill="none" stroke="url(#warm)" stroke-width="22"/>
  </svg>
  <h2 class="display services__head"><span class="tag tag--warm">Services</span> for individuals /<br>families / small groups</h2>
  <ul class="svc-list">
    <li><svg width="10" height="9" viewBox="0 0 10 9"><path d="M0 4.5 H8 M4.5 1 L8 4.5 L4.5 8" fill="none" stroke="#EA5A2A" stroke-width="1.4"/></svg>Self and Body esteem as related to disability</li>
    <li><svg width="10" height="9" viewBox="0 0 10 9"><path d="M0 4.5 H8 M4.5 1 L8 4.5 L4.5 8" fill="none" stroke="#EA5A2A" stroke-width="1.4"/></svg>Trauma and healing with a disability</li>
    <li><svg width="10" height="9" viewBox="0 0 10 9"><path d="M0 4.5 H8 M4.5 1 L8 4.5 L4.5 8" fill="none" stroke="#EA5A2A" stroke-width="1.4"/></svg>Early childhood support for disabled children and care providers</li>
    <li><svg width="10" height="9" viewBox="0 0 10 9"><path d="M0 4.5 H8 M4.5 1 L8 4.5 L4.5 8" fill="none" stroke="#EA5A2A" stroke-width="1.4"/></svg>General disability issues/peer level support</li>
    <li><svg width="10" height="9" viewBox="0 0 10 9"><path d="M0 4.5 H8 M4.5 1 L8 4.5 L4.5 8" fill="none" stroke="#EA5A2A" stroke-width="1.4"/></svg>Movement as fun for disabled kids and adults</li>
    <li><svg width="10" height="9" viewBox="0 0 10 9"><path d="M0 4.5 H8 M4.5 1 L8 4.5 L4.5 8" fill="none" stroke="#EA5A2A" stroke-width="1.4"/></svg>Moving away from therapies / assessing therapy from a disability positive perspective</li>
    <li style="border-bottom:none"><svg width="10" height="9" viewBox="0 0 10 9"><path d="M0 4.5 H8 M4.5 1 L8 4.5 L4.5 8" fill="none" stroke="#EA5A2A" stroke-width="1.4"/></svg>Accessible Recreation/Play Consults</li>
  </ul>
  <div class="cta">
    <p class="cta__ask">Interested in Working Together?</p>
    <p class="cta__contact">Contact us at abilitycrossroads.org</p>
  </div>
</section>
</body>
</html>
```